Weight Loss Challenge Social Media Graphics

Create 6-7 individual social media graphics (square size) to encourage folks to join our weight loss challenge. For the color scheme of the graphics, use the color palette attached

Note: each graphic can contain any of the stock photography attached or just the single picture of me (brown shirt) but a few should be ONLY the text
For some graphics we can say: JOIN US!
For some graphics, use only TEXT based

primarily women who want to get healthy

health and weight loss

• The largest text should be: Bright Body Reset

```html
<!DOCTYPE html>
<html lang="en">
<head>
<meta charset="utf-8">
<title>Bright Body Reset — Join Us</title>
<link rel="stylesheet" href="https://fonts.googleapis.com/css2?family=Bebas+Neue&family=Kaushan+Script&display=swap">
<style>
  :root {
    --tan: #D09A7E;
    --tan-soft: #D6A98A;
    --tan-bubble: #C7957A;
    --ink: #231F20;
    --script: #141214;
    --paper: #FFFFFF;
  }
  html, body { margin: 0; padding: 0; overflow: hidden; background: var(--paper); }
  .poster {
    position: relative;
    width: 1200px;
    height: 1200px;
    overflow: hidden;
    background: var(--paper);
    font-family: "Bebas Neue", "Oswald", sans-serif;
  }
  .backdrop-shape, .wave-band, .join-bubble { position: absolute; inset: 0; }
  .portrait {
    position: absolute;
    left: 44px;
    top: 0;
    width: 356px;
    height: 892px;
    border-radius: 170px 170px 40px 40px;
    background: linear-gradient(180deg, #6B4230 0%, #8B5A3C 14%, #C9865A 30%, #C7885E 55%, #1C1A1C 62%, #111 100%);
  }
  .title-block {
    position: absolute;
    left: 556px;
    top: 96px;
    width: 620px;
    height: 420px;
  }
  .title-main {
    margin: 0;
    color: var(--tan);
    font-size: 150px;
    font-weight: 400;
    line-height: 1;
    white-space: nowrap;
  }
  .title-script {
    position: absolute;
    left: 20px;
    top: 70px;
    margin: 0;
    font-family: "Kaushan Script", cursive;
    font-weight: 400;
    color: var(--script);
    font-size: 210px;
    line-height: 1.2;
    transform: rotate(-6deg);
    white-space: nowrap;
  }
  .challenge-name {
    position: absolute;
    left: 570px;
    top: 512px;
    margin: 0;
    color: var(--tan);
    font-size: 70px;
    font-weight: 400;
    line-height: 1;
  }
  .divider {
    position: absolute;
    left: 573px;
    top: 602px;
    width: 520px;
    height: 1px;
    background: var(--tan);
  }
  .promise {
    position: absolute;
    left: 570px;
    top: 634px;
    margin: 0;
    color: var(--tan);
    font-size: 72px;
    line-height: 0.9;
  }
  .start-date {
    position: absolute;
    left: 689px;
    top: 982px;
    margin: 0;
    color: var(--tan);
    font-size: 82px;
    line-height: 0.98;
  }
  .start-date sup { font-size: 40px; vertical-align: top; position: relative; top: 2px; }
  .join-label {
    position: absolute;
    left: 210px;
    top: 960px;
    width: 500px;
    text-align: center;
    margin: 0;
    color: var(--paper);
    font-size: 126px;
    line-height: 1;
    transform: rotate(-56deg);
  }
</style>
</head>
<body>
<main class="poster">
  <svg class="backdrop-shape" width="1200" height="1200" viewBox="0 0 1200 1200" aria-hidden="true">
    <rect x="130" y="28" width="398" height="864" rx="199" fill="var(--tan-soft)"/>
  </svg>

  <div class="portrait" role="img" aria-label="Photo of the smiling host in a caramel turtleneck and black trousers, hand on hip"></div>

  <header class="title-block">
    <h1 class="title-main">BRIGHT BODY</h1>
    <p class="title-script">Reset</p>
  </header>

  <p class="challenge-name">45 DAY CHALLENGE</p>
  <div class="divider"></div>
  <p class="promise">LOSE UP TO&nbsp; 20 POUNDS<br>IN 6 WEEKS!</p>

  <svg class="wave-band" width="1200" height="1200" viewBox="0 0 1200 1200" aria-hidden="true">
    <path d="M0,1018 C120,1000 230,1060 330,1082 C460,1110 560,1030 660,960 C780,880 880,820 1000,812 C1090,806 1160,826 1200,856 L1200,1200 L0,1200 Z" fill="var(--tan)"/>
    <path d="M0,1034 C120,1018 230,1078 330,1100 C460,1128 560,1048 660,978 C780,898 880,840 1000,832 C1090,826 1160,848 1200,878 L1200,1200 L0,1200 Z" fill="var(--ink)"/>
  </svg>

  <svg class="join-bubble" width="1200" height="1200" viewBox="0 0 1200 1200" aria-hidden="true">
    <path d="M470,894 C565,888 630,945 634,1020 C636,1050 630,1072 620,1086 L668,1092 L612,1104 C570,1160 505,1200 430,1196 C340,1190 284,1120 288,1040 C292,960 375,900 470,894 Z" fill="none" stroke="var(--tan)" stroke-width="2" stroke-dasharray="6 5"/>
    <path d="M462,910 C552,906 614,955 618,1025 C620,1052 614,1072 604,1086 L658,1090 L596,1100 C560,1150 500,1184 432,1180 C352,1175 294,1112 298,1040 C302,968 380,914 462,910 Z" fill="var(--tan-bubble)"/>
  </svg>
  <p class="join-label">JOIN US!</p>

  <p class="start-date">BEGINS MONDAY<br>JAN 6<sup>TH</sup></p>
</main>
</body>
</html>
```